Accounting firm needing business card / letterhead designed
Marcus T. Elbering, CPA
marcus@fernquill.com
www.fernquill.com
482 N Harlow Ave Ashbury Glen, OH 43719
555-555-0172

```html
<!DOCTYPE html>
<html lang="en">
<head>
<meta charset="utf-8">
<title>Fernquill – Business Card &amp; Letterhead</title>
<link href="https://fonts.googleapis.com/css2?family=Exo+2:wght@400;500;700&display=swap" rel="stylesheet">
<style>
  :root {
    --card-blue: #2f5fa6;
    --accent-green: #a6c93a;
    --deep-navy: #262a6b;
    --header-blue: #4f86c6;
    --sheet-blue: #d5e5f6;
    --footer-blue: #1f4fa0;
    --page-grey: #f2f2f2;
    --white: #ffffff;
  }
  * { margin: 0; padding: 0; box-sizing: border-box; }
  html, body {
    width: 1200px; height: 3322px; overflow: hidden;
    background: var(--white);
    font-family: "Exo 2", sans-serif;
  }
  .canvas { position: relative; width: 1200px; height: 3322px; }

  .card {
    position: absolute; left: 0; width: 1200px; height: 718px;
    background: var(--card-blue); overflow: hidden;
  }
  .card--front { top: 0; height: 760px; }
  .card--back { top: 790px; }
  .card__shapes { position: absolute; inset: 0; width: 100%; height: 100%; }

  .brand-name {
    position: absolute; font-family: "Exo 2", sans-serif;
    font-weight: 700; color: var(--deep-navy); letter-spacing: 0.04em;
    white-space: nowrap; line-height: 1;
  }
  .card--front .brand-name { left: 0; right: 0; top: 318px; text-align: center; font-size: 140px; }
  .card--back .brand-name { right: 92px; top: 80px; font-size: 84px; }

  .holder { position: absolute; left: 26px; top: 380px; color: var(--white); }
  .holder__name { font-size: 52px; font-weight: 500; color: var(--accent-green); line-height: 1.1; }
  .holder__title { font-size: 24px; margin-top: 18px; }

  .contact { position: absolute; left: 610px; top: 340px; list-style: none; color: var(--white); font-size: 27px; }
  .contact li { display: flex; align-items: center; height: 60px; }
  .contact svg { width: 32px; height: 32px; margin-right: 20px; flex: none; }
  .contact .address { display: block; height: auto; line-height: 1.45; margin-top: 4px; }

  .letterhead {
    position: absolute; left: 0; top: 1542px; width: 1200px; height: 1703px;
    background: var(--sheet-blue); overflow: hidden;
  }
  .letterhead__header {
    position: absolute; left: 0; top: 0; width: 100%; height: 127px;
    background: var(--header-blue);
  }
  .letterhead__header .brand-name { right: 30px; top: 26px; font-size: 76px; }
  .letterhead__footer { position: absolute; left: 0; bottom: 0; width: 1200px; height: 205px; }

  .page-base { position: absolute; left: 0; top: 3245px; width: 1200px; height: 77px; background: var(--page-grey); }
</style>
</head>
<body>
<main class="canvas">

  <section class="card card--front" role="img" aria-label="Business card front: blue background with a fine square pattern, green and navy corner shapes, Fernquill name">
    <svg class="card__shapes" viewBox="0 0 1200 760" aria-hidden="true">
      <polygon points="0,0 203,0 0,296" fill="var(--accent-green)"/>
      <polygon points="1200,400 1200,760 993,760" fill="var(--deep-navy)"/>
    </svg>
    <div class="brand-name">FERNQUILL</div>
  </section>

  <section class="card card--back" role="img" aria-label="Business card back: blue background with a fine square pattern and contact details">
    <svg class="card__shapes" viewBox="0 0 1200 718" aria-hidden="true">
      <polygon points="0,0 190,0 0,266" fill="var(--accent-green)"/>
      <polygon points="1200,350 1200,718 993,718" fill="var(--deep-navy)"/>
    </svg>
    <div class="brand-name">FERNQUILL</div>

    <div class="holder">
      <p class="holder__name">Marcus T. Elbering</p>
      <p class="holder__title">CPA</p>
    </div>

    <ul class="contact">
      <li>
        <svg viewBox="0 0 24 24" aria-hidden="true"><path fill="var(--accent-green)" d="M6.6 10.8a15.1 15.1 0 0 0 6.6 6.6l2.2-2.2c.3-.3.7-.4 1-.2 1.1.4 2.3.6 3.6.6.6 0 1 .4 1 1V20c0 .6-.4 1-1 1A17 17 0 0 1 3 4c0-.6.4-1 1-1h3.5c.6 0 1 .4 1 1 0 1.3.2 2.5.6 3.6.1.3 0 .7-.2 1z"/></svg>
        555-555-0172
      </li>
      <li>
        <svg viewBox="0 0 24 24" aria-hidden="true"><rect x="2" y="5" width="20" height="14" rx="1" fill="var(--accent-green)"/><path d="M2 6l10 7 10-7" fill="none" stroke="var(--card-blue)" stroke-width="1.8"/></svg>
        marcus@fernquill.com
      </li>
      <li>
        <svg viewBox="0 0 24 24" aria-hidden="true"><g fill="none" stroke="var(--accent-green)" stroke-width="2.4" stroke-linecap="round"><path d="M10 14a4 4 0 0 0 5.7 0l3.5-3.5a4 4 0 0 0-5.7-5.7l-1.2 1.2"/><path d="M14 10a4 4 0 0 0-5.7 0l-3.5 3.5a4 4 0 0 0 5.7 5.7l1.2-1.2"/></g></svg>
        www.fernquill.com
      </li>
      <li class="address">482 N Harlow Ave Ashbury Glen,<br>OH 43719</li>
    </ul>
  </section>

  <section class="letterhead" role="img" aria-label="Letterhead: light blue sheet with a faint dot pattern, header band and chevron footer">
    <header class="letterhead__header">
      <div class="brand-name">FERNQUILL</div>
    </header>
    <svg class="letterhead__footer" viewBox="0 0 1200 205" preserveAspectRatio="none" aria-hidden="true">
      <polygon points="0,0 600,78 1200,0 1200,205 0,205" fill="var(--accent-green)"/>
      <polygon points="0,30 600,118 1200,30 1200,205 0,205" fill="var(--footer-blue)"/>
    </svg>
  </section>

  <div class="page-base"></div>
</main>
</body>
</html>
```